Kolbrin new startup tech website refresh

We need a new website design for a tech startup company. We want a cutting edge high tech looking website. See kolbrin-example.com for the current site that needs to be updated with a fresh look. Use the info from the website.
We want the site to feel fast, sleek, and tech-driven while still speaking directly to the customers who will use Kolbrin. The design should highlight speed, efficiency, and precision with a monospace code font for headlines, stats, and technical details, paired with a clean sans-serif for body copy. This reinforces the product’s engineering credibility while keeping content easy to read.

Target Market(s)

tech Enterprises, Start up companies and Cloud providers

Industry/Entity Type

Tech

Number of Pages Required

2 page

Requirements
Must have
• We want the site to feel fast, sleek, and tech-driven while still speaking directly to the customers who will use Kolbrin. The design should highlight speed, efficiency, and precision with a monospace code font for headlines, stats, and technical details, paired with a clean sans-serif for body copy. This reinforces the product’s engineering credibility while keeping content easy to read.

```html
<!DOCTYPE html>
<html lang="en">
<head>
<meta charset="utf-8">
<title>Kolbrin — Accelerate Data Into Intelligence</title>
<link href="https://fonts.googleapis.com/css2?family=JetBrains+Mono:wght@600;700&family=Lato:wght@400;700&family=Arimo:wght@400;500&display=swap" rel="stylesheet">
<style>
:root{
  --navy:#1b1a8c;
  --navy-deep:#14136e;
  --ink:#333333;
  --text:#3d3d3d;
  --link:#2b2aa3;
  --lavender:#e7e7f4;
  --footer:#333333;
  --white:#ffffff;
}
*{box-sizing:border-box;margin:0;padding:0}
html,body{width:1200px;height:4505px;overflow:hidden}
body{position:relative;background:var(--white);font-family:"Lato",sans-serif;color:var(--text)}
.abs{position:absolute}
h1,h2,h3,.brand,.mono{font-family:"JetBrains Mono",monospace;font-weight:700;letter-spacing:-0.5px}

/* header */
.topline{top:0;left:0;width:1200px;height:4px;background:var(--navy-deep)}
.brand{left:110px;top:28px;font-size:54px;color:var(--navy);line-height:1;display:flex;align-items:center;gap:12px;letter-spacing:-2px}
.brand-dot{width:28px;height:28px;border-radius:50%;background:var(--navy)}
.nav{top:45px;left:0;width:1200px;font-family:"Arimo",sans-serif;font-size:14px;color:#333}
.nav a{position:absolute;top:0;height:34px;line-height:34px;text-decoration:none;color:#333;transform:translateX(-50%);white-space:nowrap}
.nav .active{background:var(--navy);color:#fff;padding:0 22px;border-radius:4px 4px 14px 4px}

/* hero */
.hero{top:115px;left:0;width:1200px;height:600px;border-bottom-left-radius:380px 360px;overflow:hidden;
  background:radial-gradient(ellipse at 32% 40%,#3a4c6a 0%,#1c2740 35%,#0c1220 75%,#080c16 100%)}
.hero h1{left:673px;top:130px;font-size:40px;line-height:55px;color:#fff;letter-spacing:-1.5px}
.hero p{left:673px;top:265px;width:420px;font-size:18.5px;line-height:30px;color:#fff}
.btn{display:block;font-family:"Arimo",sans-serif;font-size:15px;text-align:center;text-decoration:none;border-radius:4px 4px 16px 4px}
.btn-navy{background:var(--navy);color:#fff}
.btn-white{background:#fff;color:var(--navy)}
.hero .b1{left:670px;top:420px;width:130px;height:40px;line-height:40px}
.hero .b2{left:815px;top:420px;width:130px;height:40px;line-height:40px}

/* about */
.about-title{left:112px;top:802px;font-size:40px;color:var(--ink)}
.about-copy{left:112px;top:887px;width:425px;font-size:15.5px;line-height:25.8px;color:var(--text)}
.about .btn{left:112px;top:1158px;width:164px;height:44px;line-height:44px}
.about-photo{left:621px;top:810px;width:467px;height:392px;border-radius:0 200px 200px 0/0 196px 196px 0;
  background:linear-gradient(135deg,#c9ccd3 0%,#8d96a6 45%,#5b6272 100%)}

/* approach */
.approach{top:1322px;left:0;width:1200px;height:747px;background:var(--navy);border-radius:0 260px 0 320px/0 250px 0 330px}
.approach h2{left:0;width:1200px;top:104px;text-align:center;font-size:40px;color:#fff}
.approach .sub{left:0;width:1200px;top:170px;text-align:center;font-size:19px;color:#fff}
.fw-img{top:270px;width:306px;height:244px;border-radius:0 0 0 30px}
.fw-label{top:538px;width:306px;text-align:center;font-size:21px;color:#fff}
.dots{display:flex;gap:8px}
.dots span{width:24px;height:8px;border-radius:4px;background:#fff}

/* features */
.feat-title{left:0;width:1200px;top:2164px;text-align:center;font-size:40px;color:var(--ink)}
.feat-sub{left:0;width:1200px;top:2233px;text-align:center;font-size:19px;line-height:31px;color:#3d3d3d}
.ficon{width:88px;height:88px;border-radius:50%;background:var(--navy);display:flex;align-items:center;justify-content:center}
.ftext{font-size:15px;line-height:23px;color:#3d3d3d;width:215px}
.ftext.r{text-align:right}
.centre-mark{left:478px;top:2395px;width:260px;display:flex;flex-direction:column;align-items:center;gap:18px}
.centre-mark .circle{width:160px;height:160px;border-radius:50%;background:var(--navy)}
.centre-mark span{font-size:30px;color:var(--navy)}

/* blog */
.blog-title{left:0;width:1200px;top:2869px;text-align:center;font-size:40px;color:var(--ink)}
.blog-img{top:2973px;width:310px;height:224px;border-radius:6px;overflow:hidden}
.blog-h{top:3222px;font-size:20px;color:var(--link)}
.blog-p{top:3256px;width:275px;font-size:14px;line-height:22px;color:#444}
.dots.dark span{background:#999}
.dots.dark span:first-child{background:#222}

/* team */
.team{top:3449px;left:0;width:1200px;height:604px;background:linear-gradient(180deg,#e4e4f3 0%,#e9e9f5 60%,#dcdff0 100%);border-top-left-radius:230px 200px}
.team h2{left:112px;top:84px;font-size:40px;color:var(--ink)}
.team .btn{left:922px;top:94px;width:164px;height:42px;line-height:42px;font-size:14px}
.card{top:198px;width:466px;height:297px;background:#fff;border-radius:14px;border:3px solid #d6d7ea;overflow:hidden}
.card p{position:absolute;left:28px;top:36px;width:200px;font-size:16px;line-height:25.8px;color:#3d3d3d}
.card .name{position:absolute;left:28px;top:242px;font-size:18px;color:var(--link)}
.card .photo{position:absolute;right:0;top:0;width:205px;height:291px;background:linear-gradient(180deg,#c4c7cc 0%,#9da3ac 55%,#2d3340 100%)}

/* footer */
.footer{top:4053px;left:0;width:1200px;height:452px;background:var(--footer);color:#fff}
.footer h3{position:absolute;top:108px;font-size:18px}
.footer .col{position:absolute;top:158px;font-size:14px;line-height:38.5px}
.footer .col a{display:block;color:#fff;text-decoration:none}
.why{position:absolute;left:112px;top:160px;width:250px;font-size:14px;line-height:25px}
.social{position:absolute;left:112px;top:312px;width:34px;height:34px;background:var(--navy);border-radius:3px}
.contact-row{position:absolute;left:649px;display:flex;gap:20px;font-size:14px;line-height:25px}
.contact-row svg{flex:none;margin-top:4px}
.rule{position:absolute;left:112px;top:400px;width:974px;height:1px;background:#555}
.copy{position:absolute;left:0;width:1200px;top:418px;text-align:center;font-size:13px}
</style>
</head>
<body>

<div class="abs topline"></div>
<div class="abs brand"><span class="brand-dot"></span>Kolbrin</div>
<nav class="abs nav">
  <a class="active" style="left:651px">Home</a>
  <a style="left:742px">Solutions</a>
  <a style="left:843px">About Us</a>
  <a style="left:943px">Features</a>
  <a style="left:1049px">Contact Us</a>
</nav>

<section class="abs hero" role="img" aria-label="Developer in glasses working at a monitor in a dark office lit by blue screens">
  <h1 class="abs">Accelerate Data Into<br>Intelligence.</h1>
  <p class="abs">Kolbrin transforms raw data into real-time insights with unmatched speed, precision, and scalability — powering the decisions that move your business forward.</p>
  <a class="abs btn btn-navy b1">The Deck</a>
  <a class="abs btn btn-white b2">The Code</a>
</section>

<section class="about">
  <h2 class="abs about-title">About Us</h2>
  <p class="abs about-copy">Today’s AI startups promise no-code app building—but they struggle with platform code, because platforms manage resources in space and time, which requires spatial reasoning—something AI still handles poorly. As a result, AI-generated apps default to high-level platforms (e.g., serverless, managed runtimes), which are easy for AI to target but deliver unhappy trade-offs: bloated runtime overhead, poor performance, and skyrocketing costs at scale.</p>
  <a class="abs btn btn-navy">Read More</a>
  <div class="abs about-photo" role="img" aria-label="Team of three colleagues reviewing work on a laptop in a bright office"></div>
</section>

<section class="abs approach">
  <h2 class="abs">Our Approach</h2>
  <p class="abs sub">kvstack is a C service stack composed of four frameworks:</p>
  <div class="abs fw-img" style="left:112px;background:linear-gradient(135deg,#5a6c8c,#2b3a5c 60%,#1a2440)" role="img" aria-label="Engineers with a laptop beside holographic cloud service panels"></div>
  <div class="abs fw-img" style="left:446px;background:radial-gradient(circle at 55% 45%,#6a7fa6 0%,#2a3550 45%,#0d1222 100%)" role="img" aria-label="Hand holding a glowing AI chip hologram"></div>
  <div class="abs fw-img" style="left:780px;background:linear-gradient(135deg,#1a2a5a,#3a2a6a 50%,#0c1430)" role="img" aria-label="Flowing streams of coloured light data lines"></div>
  <h3 class="abs fw-label" style="left:112px">Service Framework</h3>
  <h3 class="abs fw-label" style="left:446px">Actor Framework</h3>
  <h3 class="abs fw-label" style="left:780px">Threading Framework</h3>
  <div class="abs dots" style="left:555px;top:629px"><span></span><span></span><span></span></div>
</section>

<section>
  <h2 class="abs feat-title">Key Features</h2>
  <p class="abs feat-sub">The serverless paradigm has unlocked horizontal scale but<br>sacrificed vertical scale.</p>

  <div class="abs ficon" style="left:112px;top:2359px"><svg width="50" height="50" viewBox="0 0 50 50" fill="none" stroke="#fff" stroke-width="2"><circle cx="25" cy="25" r="17"/><circle cx="25" cy="25" r="8"/><path d="M25 4v6M25 40v6M4 25h6M40 25h6"/></svg></div>
  <p class="abs ftext" style="left:220px;top:2372px">Single huge-page fault loads the entire micro-process on each I/O dispatch</p>

  <div class="abs ficon" style="left:112px;top:2533px"><svg width="50" height="50" viewBox="0 0 50 50" fill="none" stroke="#fff" stroke-width="2"><rect x="8" y="8" width="18" height="14" rx="2"/><circle cx="33" cy="33" r="9"/><path d="M17 22v10h7M33 16v8"/></svg></div>
  <p class="abs ftext" style="left:220px;top:2545px">Persistent, memory- protected mappings backed by huge pages</p>

  <div class="abs centre-mark"><div class="circle"></div><span class="mono">Kolbrin</span></div>

  <p class="abs ftext r" style="left:766px;top:2374px">104 KB footprint per actor (8 KB process + 96 KB tunable ring buffers)</p>
  <div class="abs ficon" style="left:999px;top:2359px"><svg width="50" height="50" viewBox="0 0 50 50" fill="none" stroke="#fff" stroke-width="2"><circle cx="25" cy="25" r="17"/><path d="M16 20h18M16 26h18M16 32h12"/></svg></div>

  <p class="abs ftext r" style="left:766px;top:2555px">Language-agnostic bindings (C, JavaScript, etc.)</p>
  <div class="abs ficon" style="left:999px;top:2533px"><svg width="50" height="50" viewBox="0 0 50 50" fill="none" stroke="#fff" stroke-width="2"><rect x="9" y="8" width="10" height="14"/><rect x="20" y="8" width="10" height="14"/><rect x="31" y="8" width="10" height="14"/><path d="M10 34l15-7 15 7-15 7z"/></svg></div>

  <div class="abs ficon" style="left:564px;top:2660px"><svg width="50" height="50" viewBox="0 0 50 50" fill="none" stroke="#fff" stroke-width="2"><circle cx="25" cy="25" r="16"/><path d="M15 28l6-5 5 4 9-8"/></svg></div>
  <p class="abs" style="left:0;width:1216px;text-align:center;top:2762px;font-size:15px;color:#3d3d3d">Cooperative and isolated scheduling</p>
</section>

<section>
  <h2 class="abs blog-title">Our Latest Blog</h2>
  <div class="abs blog-img" style="left:112px;background:linear-gradient(135deg,#2a3d5a,#11203a 60%,#0a1426)" role="img" aria-label="Hands typing on a laptop with a glowing AI interface"></div>
  <div class="abs blog-img" style="left:444px;background:radial-gradient(circle at 50% 45%,#3a7ad8 0%,#163a78 45%,#081632 100%)" role="img" aria-label="Glowing blue cubes rising from a circuit board"></div>
  <div class="abs blog-img" style="left:777px;background:linear-gradient(135deg,#2f4a72,#14274a 60%,#0b1630)" role="img" aria-label="Person at a laptop with holographic charts and AI overlay"></div>
  <h3 class="abs blog-h" style="left:114px">Service Framework</h3>
  <h3 class="abs blog-h" style="left:447px">Actor Framework</h3>
  <h3 class="abs blog-h" style="left:779px">Threading Framework</h3>
  <p class="abs blog-p" style="left:116px">Build data services with custom protocols using the Super-Server interface.</p>
  <p class="abs blog-p" style="left:449px">Execute soft-real-time actors for Edge AI and event-driven tasks with &lt;2ms latency.</p>
  <p class="abs blog-p" style="left:781px">Power deterministic, high-throughput coroutines (300K invocations/sec) with ...</p>
  <div class="abs dots dark" style="left:560px;top:3339px"><span style="width:22px;height:6px"></span><span style="width:22px;height:6px"></span><span style="width:22px;height:6px"></span></div>
</section>

<section class="abs team">
  <h2 class="abs">Our Team</h2>
  <a class="abs btn btn-navy">View All</a>
  <div class="abs card" style="left:112px">
    <p>Platform Development, a generalist with deep experience across all levels, from web front-ends to operating system internals. Decades of marketing technology experience.</p>
    <h3 class="name">Owen Hartley</h3>
    <div class="photo" role="img" aria-label="Portrait of a smiling man in a dark suit"></div>
  </div>
  <div class="abs card" style="left:621px">
    <p>Application Development, a prolific application developer who can build novel products on any platform. Decades of government contracting experience.</p>
    <h3 class="name">Felix Marrow</h3>
    <div class="photo" role="img" aria-label="Portrait of a bearded man in glasses and a suit"></div>
  </div>
  <div class="abs card" style="left:1130px">
    <p>Business king of Decades busin</p>
    <h3 class="name">Mira</h3>
  </div>
</section>

<footer class="abs footer">
  <h3 style="left:112px">Why Kolbrin?</h3>
  <p class="why">Zero-overhead abstractions that bring vertical scale and peak performance back to serverless.</p>
  <div class="social" aria-label="Social profile"></div>

  <h3 style="left:450px">Main Links</h3>
  <div class="col" style="left:450px"><a>Home</a><a>Platform</a><a>Solutions</a><a>Resources</a><a>About Us</a></div>

  <h3 style="left:649px">Contact Us</h3>
  <div class="contact-row" style="top:162px">
    <svg width="18" height="22" viewBox="0 0 18 22" fill="none" stroke="#fff" stroke-width="1.6"><path d="M9 21s7-7 7-12A7 7 0 0 0 2 9c0 5 7 12 7 12z"/><circle cx="9" cy="9" r="2.5"/></svg>
    <span>Alder Falls, Oregon,<br>97000, United States</span>
  </div>
  <div class="contact-row" style="top:243px">
    <svg width="18" height="18" viewBox="0 0 18 18" fill="none" stroke="#fff" stroke-width="1.6"><path d="M3 2h4l1.5 4-2 1.5a10 10 0 0 0 4 4L12 9.5l4 1.5v4a2 2 0 0 1-2 2A13 13 0 0 1 1 4a2 2 0 0 1 2-2z"/></svg>
    <span>555-014-2291</span>
  </div>
  <div class="contact-row" style="top:311px">
    <svg width="18" height="16" viewBox="0 0 18 16" fill="none" stroke="#fff" stroke-width="1.6"><rect x="1" y="2" width="16" height="12" rx="1"/><path d="M1 3l8 6 8-6"/></svg>
    <span>info@kolbrin-example.com</span>
  </div>

  <h3 style="left:955px">Other Links</h3>
  <div class="col" style="left:955px"><a>Contact Us</a><a>Careers</a><a>Cookies Policy</a><a>Terms &amp; Conditions</a><a>Privacy Policy</a></div>

  <div class="rule"></div>
  <p class="copy">Copyright © 2025 Kolbrin . All rights reserved.</p>
</footer>

</body>
</html>
```